International Consulting Firm
Stationery incl. business cards, letterhead, envelope, PPT template, and brochure
Professional
DMN QRT
CHIEF EXECUTIVE OFFICER
LEVEL 4,
7 MOOR LANE
FERN HOUSE
GOTHAM CITY
DMN@DORSETTPRYCE.EXAMPLE
WWW.DORSETTPRYCE.EXAMPLE
The fonts used in the logo are (a) Eras Bold ITC & (b)BankGothic
Logo only
This fantastic logo was designed recently by quarbin and we now need stationery to support it.

```html
<!DOCTYPE html>
<html lang="en">
<head>
<meta charset="utf-8">
<title>Dorsett Pryce Stationery</title>
<link href="https://fonts.googleapis.com/css2?family=Roboto:wght@400;700;900&display=swap" rel="stylesheet">
<style>
  :root {
    --ink: #111111;
    --paper: #ffffff;
    --stage: #dcd9d5;
    --grey: #8a8a8a;
    --shadow: rgba(0,0,0,0.25);
  }
  * { margin: 0; padding: 0; box-sizing: border-box; }
  html, body { width: 1200px; height: 908px; overflow: hidden; }
  body { background: var(--stage); font-family: "Roboto", Arial, sans-serif; color: var(--ink); position: relative; }
  .piece { position: absolute; background: var(--paper); overflow: hidden; box-shadow: 0 3px 10px var(--shadow); }
  .dark { background: var(--ink); color: var(--paper); }
  .abs { position: absolute; }
  .mark { position: absolute; border-radius: 50%; }
  .mark--white { background: var(--paper); }
  .mark--black { background: var(--ink); }
  .brand { position: absolute; font-weight: 700; letter-spacing: 1px; white-space: nowrap; }
  .brand--dark { color: var(--ink); }
  .brand--light { color: var(--paper); }
  .tiny { font-size: 6px; line-height: 1.5; }
  .small { font-size: 8px; line-height: 1.45; }

  /* business card front */
  .card-front { left: 95px; top: 100px; width: 280px; height: 162px; }
  .card-front .block { left: 0; top: 0; width: 130px; height: 118px; background: var(--ink); border-bottom-right-radius: 70px; }
  .card-front .details { right: 14px; top: 14px; text-align: right; }
  .card-front .name { font-size: 13px; font-weight: 700; }
  .card-front .title { font-size: 7px; font-weight: 700; margin-bottom: 6px; }

  /* business card back */
  .card-back { left: 95px; top: 305px; width: 280px; height: 160px; }
  .card-back .web { left: 0; right: 0; top: 118px; text-align: center; font-size: 9px; font-weight: 700; letter-spacing: 1px; }

  /* letterhead */
  .letterhead { left: 437px; top: 105px; width: 218px; height: 350px; }
  .letterhead .address { right: 14px; top: 20px; width: 80px; }
  .letterhead .body { left: 22px; top: 90px; width: 172px; }
  .letterhead .body p { margin-bottom: 8px; }
  .letterhead .foot { right: -40px; bottom: -60px; width: 200px; height: 110px; border-radius: 50%; background: var(--ink); }
  .letterhead .web { right: 12px; bottom: 10px; font-size: 6px; color: var(--paper); font-weight: 700; }

  /* brochures */
  .brochure { display: flex; }
  .panel { position: relative; flex: 1; overflow: hidden; }
  .panel + .panel { border-left: 1px solid #d0d0d0; }
  .about-title { font-size: 15px; font-weight: 700; display: flex; align-items: center; gap: 6px; margin: 12px 10px 10px; }
  .about-title i { width: 12px; height: 12px; border-radius: 50%; display: inline-block; }
  .about-text { margin: 0 10px; }
  .brochure-out { left: 750px; top: 125px; width: 412px; height: 288px; }
  .brochure-in { left: 750px; top: 425px; width: 412px; height: 275px; }

  /* presentation */
  .slide { height: 210px; }
  .slide-one { left: 88px; top: 520px; width: 288px; }
  .slide-two { left: 412px; top: 520px; width: 300px; }
  .slide .heading { font-size: 21px; font-weight: 900; line-height: 1.1; }
</style>
</head>
<body>

<!-- business card front -->
<section class="piece card-front">
  <div class="abs block"></div>
  <div class="mark mark--white" style="left:28px;top:18px;width:60px;height:60px;"></div>
  <div class="brand brand--dark" style="left:14px;top:128px;font-size:11px;">DORSETTPRYCE</div>
  <div class="abs details">
    <div class="name">DMN QRT</div>
    <div class="title">CHIEF EXECUTIVE OFFICER</div>
    <div class="tiny">LEVEL 4,<br>7 MOOR LANE<br>FERN HOUSE<br>GOTHAM CITY<br>T +1 555 0100<br>F +1 555 0101<br>M +1 555 0102<br>DMN@DORSETTPRYCE.EXAMPLE</div>
  </div>
</section>

<!-- business card back -->
<section class="piece dark card-back">
  <div class="mark mark--white" style="left:110px;top:28px;width:60px;height:60px;"></div>
  <div class="abs web">WWW.DORSETTPRYCE.EXAMPLE</div>
</section>

<!-- letterhead -->
<section class="piece letterhead">
  <div class="mark mark--black" style="left:22px;top:20px;width:20px;height:20px;"></div>
  <div class="brand brand--dark" style="left:22px;top:46px;font-size:8px;">DORSETTPRYCE</div>
  <div class="abs address tiny">LEVEL 4,<br>7 MOOR LANE<br>FERN HOUSE<br>GOTHAM CITY<br>T +1 555 0100</div>
  <div class="abs body tiny">
    <p>Dear Client,</p>
    <p>We thank you for your interest in our consulting services and look forward to working with you on the next stage of your project.</p>
    <p>Kind regards,</p>
    <p><strong>DMN QRT</strong></p>
  </div>
  <div class="abs foot"></div>
  <div class="abs web">WWW.DORSETTPRYCE.EXAMPLE</div>
</section>

<!-- brochure outside -->
<section class="piece brochure brochure-out">
  <div class="panel">
    <div class="about-title"><i class="mark--black"></i>About us</div>
    <p class="about-text small">We are an international consulting firm helping clients plan, grow and deliver lasting results across every market we serve.</p>
  </div>
  <div class="panel dark">
    <div class="mark mark--white" style="left:-30px;top:20px;width:170px;height:170px;"></div>
    <div class="brand brand--light" style="left:14px;top:220px;font-size:10px;">DORSETTPRYCE</div>
  </div>
  <div class="panel">
    <div class="abs dark" style="left:0;top:0;width:100%;height:200px;border-bottom-left-radius:90px;"></div>
    <div class="mark mark--white" style="left:40px;top:50px;width:56px;height:56px;"></div>
    <div class="abs tiny" style="left:0;right:0;bottom:22px;text-align:center;font-weight:700;">WWW.DORSETTPRYCE.EXAMPLE</div>
  </div>
</section>

<!-- brochure inside -->
<section class="piece brochure brochure-in">
  <div class="panel dark">
    <div class="about-title"><i class="mark--white"></i>About us</div>
    <p class="about-text small">We are an international consulting firm helping clients plan, grow and deliver lasting results across every market we serve.</p>
  </div>
  <div class="panel">
    <div class="mark mark--black" style="left:50px;top:60px;width:36px;height:36px;"></div>
    <div class="brand brand--dark" style="left:24px;top:104px;font-size:8px;">DORSETTPRYCE</div>
    <div class="mark" style="left:-20px;top:170px;width:90px;height:90px;background:#cfcfcf;"></div>
  </div>
  <div class="panel">
    <div class="mark mark--black" style="left:30px;top:30px;width:76px;height:76px;"></div>
    <div class="abs tiny" style="left:0;right:0;bottom:22px;text-align:center;font-weight:700;">WWW.DORSETTPRYCE.EXAMPLE</div>
  </div>
</section>

<!-- presentation slide one -->
<section class="piece slide slide-one">
  <div class="abs dark" style="left:0;top:0;width:135px;height:100%;"></div>
  <div class="mark mark--white" style="left:-40px;top:-30px;width:150px;height:150px;"></div>
  <div class="brand brand--light" style="left:12px;top:160px;font-size:10px;">DORSETTPRYCE</div>
  <div class="abs heading" style="left:150px;top:60px;">Wecome to our<br>Presentation</div>
</section>

<!-- presentation slide two -->
<section class="piece slide slide-two">
  <div class="abs dark" style="left:0;top:0;width:110px;height:100%;border-top-right-radius:60px;border-bottom-right-radius:60px;"></div>
  <div class="mark mark--white" style="left:18px;top:55px;width:70px;height:70px;"></div>
  <div class="abs heading" style="left:130px;top:40px;">Wecome to our<br>Presentation</div>
</section>

</body>
</html>
```